Ferris Contracting LLC Business Card Design

I am looking for a creative and unique business card design. We are a commercial construction general contractor. With the name "FERRIS" Contracting, I am hoping to see some neat designs that correlate with the name.

```html
<!DOCTYPE html>
<html lang="en">
<head>
<meta charset="utf-8">
<title>Ferris Contracting LLC – Business Card</title>
<link href="https://fonts.googleapis.com/css2?family=Poppins:wght@400;500;700&display=swap" rel="stylesheet">
<style>
  :root {
    --page-bg: #1a1b1e;
    --card-bg: #25272b;
    --card-edge: #2e3035;
    --brand-blue: #1e8fe0;
    --text-light: #d6d9de;
    --text-muted: #b3b7bd;
    --rule: #c9ccd1;
  }
  * { margin: 0; padding: 0; box-sizing: border-box; }
  html, body {
    width: 1200px; height: 800px; overflow: hidden;
    background: var(--page-bg);
    font-family: "Poppins", sans-serif;
  }
  .canvas {
    position: relative; width: 1200px; height: 800px;
    display: flex; flex-direction: column; align-items: center; justify-content: center; gap: 56px;
  }
  .card {
    position: relative; width: 540px; height: 308px;
    background: var(--card-bg);
    border: 1px solid var(--card-edge);
    border-radius: 18px;
    box-shadow: 0 18px 40px rgba(0,0,0,.45);
    overflow: hidden;
  }
  .brand {
    display: flex; align-items: center; gap: 12px;
    color: var(--brand-blue); font-weight: 700; letter-spacing: .5px;
  }
  .brand-dot { width: 14px; height: 14px; border-radius: 50%; background: var(--brand-blue); }
  .card-front .brand {
    position: absolute; left: 50%; top: 50%; transform: translate(-50%, -50%);
    font-size: 34px; white-space: nowrap;
  }
  .card-back .brand {
    position: absolute; right: 34px; top: 46px; font-size: 24px; white-space: nowrap;
  }
  .person { position: absolute; left: 34px; top: 160px; }
  .person-name { color: var(--brand-blue); font-weight: 700; font-size: 22px; letter-spacing: .5px; line-height: 1.1; }
  .person-title { color: var(--text-light); font-size: 12px; font-weight: 400; margin-top: 2px; }
  .divider {
    position: absolute; left: 196px; right: 34px; top: 190px; height: 1px; background: var(--rule);
  }
  .contact { position: absolute; left: 34px; bottom: 28px; list-style: none; }
  .contact li {
    display: flex; align-items: center; gap: 10px;
    color: var(--text-light); font-size: 13px; line-height: 22px;
  }
  .contact-icon {
    width: 16px; height: 16px; border-radius: 50%; background: var(--brand-blue);
    display: flex; align-items: center; justify-content: center; flex-shrink: 0;
  }
  .address {
    position: absolute; right: 34px; top: 206px; text-align: right;
    color: var(--text-muted); font-size: 12px; line-height: 18px;
  }
</style>
</head>
<body>
<main class="canvas">
  <section class="card card-front" aria-label="Card front">
    <div class="brand"><span class="brand-dot"></span>FERRIS CONTRACTING</div>
  </section>

  <section class="card card-back" aria-label="Card back">
    <div class="brand"><span class="brand-dot"></span>FERRIS CONTRACTING</div>

    <div class="person">
      <p class="person-name">MARCUS T REED</p>
      <p class="person-title">CEO</p>
    </div>
    <div class="divider"></div>

    <ul class="contact">
      <li>
        <span class="contact-icon">
          <svg width="9" height="9" viewBox="0 0 24 24"><path fill="#fff" d="M6.6 10.8a15.1 15.1 0 0 0 6.6 6.6l2.2-2.2c.3-.3.7-.4 1-.2 1.1.4 2.3.6 3.6.6.6 0 1 .4 1 1V20c0 .6-.4 1-1 1C10.6 21 3 13.4 3 4c0-.6.4-1 1-1h3.5c.6 0 1 .4 1 1 0 1.3.2 2.5.6 3.6.1.3 0 .7-.2 1z"/></svg>
        </span>(480) 555-0142
      </li>
      <li>
        <span class="contact-icon">
          <svg width="9" height="9" viewBox="0 0 24 24"><path fill="#fff" d="M2 5h20v14H2z"/><path fill="none" stroke="#1e8fe0" stroke-width="2" d="M2 5l10 8 10-8"/></svg>
        </span>info@ferrisbuild.com
      </li>
      <li>
        <span class="contact-icon">
          <svg width="10" height="10" viewBox="0 0 24 24" fill="none" stroke="#fff" stroke-width="2"><circle cx="12" cy="12" r="9"/><path d="M3 12h18M12 3c3 3 3 15 0 18M12 3c-3 3-3 15 0 18"/></svg>
        </span>www.ferrisbuild.com
      </li>
    </ul>

    <address class="address" style="font-style:normal">
      4820 E. Mesa Ridge Rd.<br>
      Suite 210, Arizona 85004
    </address>
  </section>
</main>
</body>
</html>
```